Online Digital Solutions Agency needs a New Business Card

We are a Online/Digital solution agency. We provide WordPress Solutions, Online & Digital Marketing Solutions including SEO, Social Media Marketing and Managed Hosting including VPS and Cloud Hosting solutions. We also design and build bespoke web sites and web applications for various clients. We are very good at site migrations, 3rd party API integrations and mobile app development.

We are rebranding our agency and have already designed a new logo. We have selected 5-6 colours as our base colour and are currently building our new website based around these colour scheme.

Our logo indicates that we are a cloud solution providers, and (i.e. the Clouds), and developers (i.e. HTML Tags, and CSS formats). We use the 5-6 base colours and use various shades of these colours as required.

Our old website is located at: www.brambleforgelabs.com

And our new website is going to be at (we are working on it at the moment ...):
https://creative.brambleforgelabs.co.uk/

Our slogan is "Digital Transformation Specialist"

What we mean by that is; we can take any existing business and get them up and transform them in to the digital world, starting with Hosting, Web Design, Development & Online Marketing aspects.

The powerpoint is a document that we use to present our projects to clients at the moment, and the cloud is on the background as we clarified earlier. (Just to get the idea)

What we are looking for is a Great WoW factor design to start with, ideally with the Logo and Logo colour scheme if possible but not required as long as the designers can do better, and basically give life to our logo and company via the Business card design.

Ideally with some icons perhaps to indicate the address, location, mobile, email, and website would be good but again optional as long as there is a good design.

The cloud can be used as a background if required in a light shade or as a watermark share perhaps.

The logos' and the Illustrator files are shared with you so you can use them as required.

Ideally the business card should have a Name, title, Mobile, Email , Website, Address and perhaps some social media links.

Target Market(s)

New Startups, SME's, Contract and Outsource Clients

Contact Information for Business Card

Company Name:
==============
BrambleForge Labs (UK) Ltd.

Tag Line:
========
“Digital Transformation Specialists”

Adress:
=======

Suite KR73054
14-16 Ashgrove Lane
London
E9 4PD.

Name:
=====
Idris Malek

Title: (Optional)
=============
FQTA, PgD (RNOM)

Role:
=====
Digital Solutions Architect

Email:
=====
idris@brambleforgelabs.uk

WebSite:
=======
http://www.brambleforgelabs.uk

OR

www.brambleforgelabs.uk

Mobile:
======
0044 (0)75 218 30479

OR

+44 (0)75 218 30479

LinkedIN: (Optional)
========
https://uk.linkedin.com/in/idrismalek

Skype: (Optional)
======
idris.malek

Twitter (Optional) : idrismalek

Font styles to use
Serif
Sans Serif

Requirements
Must have
• The Logo
• Business Name
• Person Name
• Title
• Mobile
• Email
• Website
• Address
• I have provided the colour scheme on my files.
Nice to have
• Twiter
• Linked in
• Facebook

```html
<!DOCTYPE html>
<html lang="en">
<head>
<meta charset="utf-8">
<title>BrambleForge Labs – Business Card</title>
<link rel="stylesheet" href="https://fonts.googleapis.com/css2?family=Roboto:wght@400;500;700&display=swap">
<style>
  :root {
    --page-bg: #e4e4e4;
    --card-white: #f7f7f7;
    --brand-blue: #0b5aa6;
    --brand-deep: #0a5cad;
    --brand-sky: #4fd3f5;
    --accent-orange: #f7a81b;
    --text-grey: #4a4a4a;
    --icon-blue: #1e6fb8;
    --white: #ffffff;
  }
  * { margin: 0; padding: 0; box-sizing: border-box; }
  html, body {
    width: 1125px; height: 1200px; overflow: hidden;
    background: var(--page-bg);
    font-family: "Roboto", Arial, sans-serif;
  }
  .card {
    position: absolute; left: 171px; width: 826px; height: 472px;
    box-shadow: 0 2px 5px rgba(0,0,0,0.25);
  }
  /* Front */
  .card-front { top: 106px; background: var(--card-white); }
  .brand-name {
    position: absolute; left: 80px; top: 112px;
    font-size: 32px; font-weight: 700; color: var(--brand-blue); letter-spacing: -0.3px;
  }
  .tagline {
    position: absolute; left: 54px; top: 172px;
    font-size: 13px; font-weight: 400; letter-spacing: 0.4px;
    color: var(--text-grey); text-transform: uppercase;
  }
  .address {
    position: absolute; left: 54px; top: 252px;
    font-size: 20px; line-height: 25px; color: var(--text-grey); font-style: normal;
  }
  .contact-list { position: absolute; left: 54px; top: 340px; list-style: none; }
  .contact-list li {
    display: flex; align-items: center; height: 26.5px;
    font-size: 20px; color: var(--text-grey);
  }
  .contact-list svg { width: 18px; height: 18px; margin-right: 12px; fill: var(--icon-blue); }
  .person { position: absolute; right: 52px; top: 288px; text-align: right; }
  .person-name { font-size: 30px; font-weight: 700; color: var(--brand-blue); line-height: 36px; letter-spacing: 0.3px; }
  .person-creds, .person-role { font-size: 21px; color: var(--accent-orange); line-height: 26px; }

  /* Back */
  .card-back {
    top: 639px; color: var(--white);
    background: radial-gradient(ellipse 520px 360px at 50% 45%, var(--brand-sky) 0%, #2aa6e2 45%, var(--brand-deep) 100%);
  }
  .social-list {
    position: absolute; left: 57px; top: 66px; list-style: none;
    display: flex; gap: 14px; font-size: 20px;
  }
  .social-list li { display: flex; align-items: center; }
  .social-list .dot {
    width: 14px; height: 14px; border-radius: 50%; background: var(--white); margin-right: 7px;
  }
  .back-brand {
    position: absolute; left: 57px; top: 350px;
    font-size: 36px; font-weight: 700; letter-spacing: -0.3px;
  }
  .back-site {
    position: absolute; right: 46px; top: 371px; font-size: 19px;
  }
</style>
</head>
<body>
  <section class="card card-front">
    <div class="brand-name">BrambleForge Labs</div>
    <div class="tagline">Digital Transformation Specialists</div>

    <address class="address">14-16 Ashgrove Lane<br>London, E9 4PD<br>United Kingdom</address>

    <ul class="contact-list">
      <li>
        <svg viewBox="0 0 18 18"><path d="M5 1h8a1 1 0 0 1 1 1v14a1 1 0 0 1-1 1H5a1 1 0 0 1-1-1V2a1 1 0 0 1 1-1zm1 2v10h6V3zm3 11.2a.9.9 0 1 0 0 1.8.9.9 0 0 0 0-1.8z"/></svg>
        +44 (0)75 218 30479
      </li>
      <li>
        <svg viewBox="0 0 18 18"><path d="M1 4h16v10H1zm1.6 1.2L9 10l6.4-4.8z"/></svg>
        idris@brambleforgelabs.uk
      </li>
      <li>
        <svg viewBox="0 0 18 18"><circle cx="9" cy="9" r="8"/><path d="M5 6c2-1 3 1 4 2s0 3-2 3-1 3-1 4M11 3c0 2 2 2 3 3s-1 3 0 5" stroke="#f7f7f7" stroke-width="1.4" fill="none"/></svg>
        www.brambleforgelabs.uk
      </li>
    </ul>

    <div class="person">
      <div class="person-name">IDRIS MALEK</div>
      <div class="person-creds">FQTA, PgD (RNOM)</div>
      <div class="person-role">Digital Solutions Architect</div>
    </div>
  </section>

  <section class="card card-back">
    <ul class="social-list">
      <li><span class="dot"></span>/idrismalek</li>
      <li><span class="dot"></span>idris.malek</li>
      <li><span class="dot"></span>idrismalek</li>
    </ul>
    <div class="back-brand">BrambleForge Labs</div>
    <div class="back-site">www.brambleforgelabs.uk</div>
  </section>
</body>
</html>
```